Wealth management firm needs a business card design

Using my logo, create a business card that covers all of the regulatory wordings that I need. It must have - Registered Office 7-9 Pelgrove Wynd, Edinburgh, EH4 2QN. Registered in Scotland under number SC804317. VORELT Wealth Management Ltd is an appointed representative of Kestoby wealth management Ltd, which is authorised and regulated by the Monetary Oversight Council.

Target Market(s)

professional clients

Industry/Entity Type

finance

Contact Information for Business Card

VORELT Wealth Management, Conor Tresk-Whitlaw, Director, 5 Dunmore Row, Edinburgh, EH9 4RT. 07812 459 163, conor.tresk-whitlaw@vorelt-example.com , www.vorelt-example.com

Font styles to use
Serif

Colors
0054AA
0677BA
7BADD7
CADEEF
E8F1F8

Requirements
Must have
• regulatory wording in small text at bottom

```html
<!DOCTYPE html>
<html lang="en">
<head>
<meta charset="utf-8">
<title>VORELT Wealth Management – Business Card</title>
<link rel="stylesheet" href="https://fonts.googleapis.com/css2?family=Montserrat:wght@400;500;600&family=Noto+Serif:wght@400&display=swap">
<style>
  :root {
    --backdrop: #e6e6e8;
    --card-white: #ffffff;
    --brand-blue: #3d73bb;
    --text-dark: #1e1e1e;
    --photo-light: #c9b7a6;
    --photo-dark: #2b3244;
  }
  * { margin: 0; padding: 0; box-sizing: border-box; }
  html, body {
    width: 1200px; height: 1108px; overflow: hidden;
    background: var(--backdrop);
  }
  body { position: relative; font-family: "Montserrat", Arial, sans-serif; }

  .card { position: absolute; width: 740px; height: 443px; overflow: hidden; }
  .card-front { left: 241px; top: 68px; background: var(--card-white); }
  .card-back { left: 248px; top: 589px; background: var(--brand-blue); color: var(--card-white); }

  .brand { position: absolute; text-align: center; font-family: "Noto Serif", Georgia, serif; }
  .brand-mark { display: block; margin: 0 auto; border-radius: 50%; }
  .brand-name { display: block; font-weight: 400; white-space: nowrap; }
  .brand-tagline { display: block; font-family: "Noto Serif", Georgia, serif; }

  .card-front .brand { left: 0; width: 414px; top: 34px; }
  .card-front .brand-mark { width: 56px; height: 56px; background: var(--brand-blue); margin-bottom: 22px; }
  .card-front .brand-name { font-size: 24px; color: var(--text-dark); line-height: 1.1; }
  .card-front .brand-tagline { font-size: 9px; color: var(--text-dark); margin-top: 2px; }

  .contact { position: absolute; left: 52px; top: 203px; color: var(--text-dark); }
  .contact-name { font-size: 25px; font-weight: 600; color: var(--brand-blue); line-height: 1.2; }
  .contact-role { font-size: 16px; margin-top: 2px; }
  .contact-address { font-size: 16px; margin-top: 14px; }
  .contact-list { list-style: none; margin-top: 8px; }
  .contact-list li { display: flex; align-items: center; font-size: 16px; height: 21px; }
  .contact-list svg { width: 16px; height: 14px; margin-right: 13px; fill: var(--brand-blue); flex: none; }

  .front-band {
    position: absolute; left: 0; right: 0; bottom: 0; height: 50px;
    background: var(--brand-blue); color: var(--card-white);
    font-size: 16px; padding-left: 92px; line-height: 50px;
  }
  .portrait {
    position: absolute; left: 437px; top: 0; width: 303px; height: 443px;
    background: linear-gradient(180deg, var(--card-white) 0%, var(--photo-light) 45%, var(--photo-dark) 100%);
  }

  .card-back .brand { left: 0; right: 0; top: 60px; }
  .card-back .brand-mark { width: 110px; height: 110px; border: 3px solid var(--card-white); margin-bottom: 24px; }
  .card-back .brand-name { font-size: 36px; line-height: 1.2; }
  .card-back .brand-tagline { font-size: 15px; margin-top: 4px; }

  .regulatory {
    position: absolute; left: 0; right: 0; top: 295px;
    text-align: center; font-size: 15.5px; line-height: 21px; font-weight: 500;
  }
</style>
</head>
<body>
  <section class="card card-front">
    <div class="brand">
      <span class="brand-mark"></span>
      <span class="brand-name">VORELT Wealth Management Ltd</span>
      <span class="brand-tagline">Personal Financial Advice</span>
    </div>

    <div class="contact">
      <p class="contact-name">Conor Tresk-Whitlaw</p>
      <p class="contact-role">Director</p>
      <p class="contact-address">5 Dunmore Row, Edinburgh, EH9 4RT</p>
      <ul class="contact-list">
        <li>
          <svg viewBox="0 0 16 14" aria-hidden="true"><path d="M1 4c0-2 3-3 7-3s7 1 7 3v1h-3V4H4v1H1zM3 6h10l2 7H1z"/></svg>
          07812 459 163
        </li>
        <li>
          <svg viewBox="0 0 16 14" aria-hidden="true"><path d="M0 2h16v1L8 8 0 3zM0 5l8 5 8-5v8H0z"/></svg>
          conor.tresk-whitlaw@vorelt-example.com
        </li>
        <li>
          <svg viewBox="0 0 16 14" aria-hidden="true"><circle cx="8" cy="7" r="6.5"/></svg>
          www.vorelt-example.com
        </li>
      </ul>
    </div>

    <div class="front-band">www.vorelt-example.com</div>
    <div class="portrait" role="img" aria-label="Portrait photograph of the director in a suit and striped shirt"></div>
  </section>

  <section class="card card-back">
    <div class="brand">
      <span class="brand-mark"></span>
      <span class="brand-name">VORELT Wealth Management Ltd</span>
      <span class="brand-tagline">Personal Financial Advice</span>
    </div>
    <div class="regulatory">
      <p>Registered Office 7-9 Pelgrove Wynd, Edinburgh, EH4 2QN.</p>
      <p>Registered in Scotland under number SC804317.</p>
      <p>VORELT Wealth Management Ltd is an appointed representative</p>
      <p>of Kestoby wealth management Ltd, which is authorised</p>
      <p>and regulated by the Monetary Oversight Council.</p>
    </div>
  </section>
</body>
</html>
```